New boutique IT consultancy needs business card

I need a business card and logo for my IT consultancy business, called 'Quenbrylle' . I want it to make me look bigger than I am. I want it to look classy, and modern. Simple design, that will be easy for me to translate into my webpage etc. The business card should be bold, and different.

The logo should emphasise the 'y' as used in quenbrylle

Target Market(s)

IT divisions in other companies

Industry/Entity Type

Business

Contact Information for Business Card

Marcel Thornby
Director
+61 437 819 063
mthornby@quenbrylle-mail.com

```html
<!DOCTYPE html>
<html lang="en">
<head>
<meta charset="utf-8">
<title>Quenbrylle — Business Card</title>
<link href="https://fonts.googleapis.com/css2?family=Open+Sans:wght@400;600;700&display=swap" rel="stylesheet">
<style>
  :root {
    --bg: #e9e7e2;
    --card-white: #f7f7f6;
    --card-white-edge: #e6e6e4;
    --green: #8cc63f;
    --green-deep: #6aa829;
    --green-light: #b2dc5e;
    --ink: #555555;
    --ink-soft: #777777;
    --rule: #bdbdbd;
    --white: #ffffff;
  }
  * { box-sizing: border-box; margin: 0; padding: 0; }
  html, body { width: 1200px; height: 780px; overflow: hidden; }
  body {
    background: var(--bg);
    font-family: "Open Sans", Arial, sans-serif;
    display: flex;
    align-items: center;
    justify-content: center;
    gap: 40px;
  }
  .card {
    width: 540px;
    height: 310px;
    border-radius: 22px;
    position: relative;
    box-shadow: 0 2px 0 rgba(0,0,0,0.06), 0 14px 30px rgba(0,0,0,0.12);
  }
  .card--front {
    background: linear-gradient(135deg, var(--white) 0%, var(--card-white) 60%, var(--card-white-edge) 100%);
  }
  .card--back {
    background: radial-gradient(circle at 55% 45%, var(--green-light) 0%, var(--green) 50%, var(--green-deep) 100%);
    display: flex;
    align-items: center;
    justify-content: center;
  }
  .brand {
    position: absolute;
    left: 40px;
    top: 0;
    bottom: 0;
    width: 170px;
    display: flex;
    align-items: center;
    justify-content: center;
    gap: 8px;
  }
  .brand__dot {
    width: 12px;
    height: 12px;
    border-radius: 50%;
    background: var(--green);
  }
  .brand__name {
    font-weight: 600;
    font-size: 24px;
    color: var(--green);
    letter-spacing: 0.5px;
  }
  .divider {
    position: absolute;
    left: 232px;
    top: 58px;
    bottom: 58px;
    width: 1px;
    background: var(--rule);
  }
  .identity {
    position: absolute;
    left: 270px;
    top: 70px;
  }
  .identity__name {
    font-weight: 700;
    font-size: 24px;
    color: var(--green);
    line-height: 1.1;
  }
  .identity__title {
    font-size: 15px;
    color: var(--ink);
    margin-top: 2px;
  }
  .contact {
    position: absolute;
    left: 270px;
    bottom: 70px;
    list-style: none;
    font-size: 14px;
    color: var(--ink);
  }
  .contact__item {
    display: flex;
    align-items: center;
    gap: 8px;
    margin-top: 6px;
  }
  .contact__icon {
    width: 18px;
    height: 18px;
    background: var(--green);
    border-radius: 3px;
    flex: none;
  }
  .brand--reverse .brand__name {
    font-size: 40px;
    font-weight: 600;
    color: var(--white);
    letter-spacing: 1px;
  }
</style>
</head>
<body>
  <section class="card card--front" aria-label="Business card front">
    <div class="brand">
      <span class="brand__dot"></span>
      <span class="brand__name">Quenbrylle</span>
    </div>
    <div class="divider"></div>
    <div class="identity">
      <p class="identity__name">Marcel Thornby</p>
      <p class="identity__title">Director</p>
    </div>
    <ul class="contact">
      <li class="contact__item">
        <svg class="contact__icon" viewBox="0 0 18 18" aria-hidden="true">
          <path d="M6 4.5l1.6 2.6-1 1.2c.7 1.4 1.7 2.4 3.1 3.1l1.2-1 2.6 1.6-.6 1.6c-.3.6-1 .9-1.6.7C7.6 13.2 4.8 10.4 3.7 6.7c-.2-.6.1-1.3.7-1.6z" fill="#ffffff"/>
        </svg>
        <span>+61 437 819 063</span>
      </li>
      <li class="contact__item">
        <svg class="contact__icon" viewBox="0 0 18 18" aria-hidden="true">
          <rect x="4" y="5.5" width="10" height="7" fill="none" stroke="#ffffff" stroke-width="1.3"/>
          <path d="M4 5.5l5 4 5-4" fill="none" stroke="#ffffff" stroke-width="1.3"/>
        </svg>
        <span>mthornby@quenbrylle-mail.com</span>
      </li>
    </ul>
  </section>

  <section class="card card--back" aria-label="Business card back">
    <div class="brand brand--reverse" style="position:static;width:auto;">
      <span class="brand__name">Quenbrylle</span>
    </div>
  </section>
</body>
</html>
```